Redesign Colorful Business Card

Please redesign the card attached. It is too busy. Please don't eliminate any of the words. The repetivite word "free" can be used less often.

Target Market(s)

College Students.

Contact Information for Business Card

The details listed in the attached image

Font styles to use
Sans Serif

Requirements
Must have
• A clear and simple presentation and must be attractive.

```html
<!DOCTYPE html>
<html lang="en">
<head>
<meta charset="utf-8">
<title>Study Brisk – Card</title>
<link href="https://fonts.googleapis.com/css2?family=Bebas+Neue&family=Montserrat:wght@700&display=swap" rel="stylesheet">
<style>
  :root {
    --page-bg: #dcdcdc;
    --card-bg: #e8e8e8;
    --ink: #1a1a1a;
    --white: #ffffff;
    --blue-a: #1565ad;
    --blue-b: #3d9ad6;
    --blue: #1f74bf;
    --orange-a: #e07b22;
    --orange-b: #f0b42a;
    --orange: #e8882a;
    --green-a: #2f9e3c;
    --green-b: #8cc63f;
    --green: #56b140;
  }
  * { margin: 0; padding: 0; box-sizing: border-box; }
  html, body { width: 1200px; height: 1051px; overflow: hidden; }
  body { background: var(--page-bg); position: relative; }

  .card {
    position: absolute;
    left: 0; top: 182px;
    width: 1200px; height: 686px;
    background: var(--card-bg);
  }

  .brand {
    position: absolute;
    left: 0; right: 0; top: 150px;
    display: flex; justify-content: center; align-items: center; gap: 22px;
  }
  .brand-dot {
    width: 58px; height: 58px; border-radius: 50%;
    background: var(--blue);
  }
  .brand-name {
    font-family: "Montserrat", sans-serif;
    font-weight: 700;
    font-size: 76px;
    line-height: 1;
    color: var(--ink);
  }

  .banner {
    position: absolute;
    top: 360px;
    width: 372px; height: 275px;
  }
  .banner--time { left: 43px; --ribbon-a: var(--blue-a); --ribbon-b: var(--blue-b); --accent: var(--green); --horn: var(--blue); }
  .banner--memory { left: 415px; --ribbon-a: var(--orange-a); --ribbon-b: var(--orange-b); --accent: var(--blue); --horn: var(--orange); }
  .banner--class { left: 787px; --ribbon-a: var(--green-a); --ribbon-b: var(--green-b); --accent: var(--orange); --horn: var(--green); }

  .banner svg { width: 372px; height: 275px; overflow: visible; }
  .stop-a { stop-color: var(--ribbon-a); }
  .stop-b { stop-color: var(--ribbon-b); }
  .accent { fill: var(--accent); }
  .tag-label, .free-label, .claim {
    font-family: "Bebas Neue", sans-serif;
    fill: var(--white);
  }
  .tag-label { font-size: 26px; letter-spacing: 0.5px; }
  .free-label { font-size: 30px; letter-spacing: 1px; }
  .claim { font-size: 32px; letter-spacing: 0.3px; }

  .megaphone {
    position: absolute;
    left: 88px; top: 200px;
    width: 62px; height: 62px;
    border-radius: 14px;
    background: linear-gradient(135deg, var(--white), var(--horn));
  }
</style>
</head>
<body>
  <div class="card">
    <div class="brand">
      <span class="brand-dot"></span>
      <span class="brand-name">Study Brisk</span>
    </div>

    <div class="banner banner--time">
      <svg viewBox="0 0 372 275">
        <defs>
          <linearGradient id="ribbon-time" x1="0" y1="1" x2="1" y2="0">
            <stop offset="0" class="stop-a"/><stop offset="1" class="stop-b"/>
          </linearGradient>
        </defs>
        <polygon points="0,84 352,33 352,153 0,202" fill="url(#ribbon-time)"/>
        <polygon points="120,186 148,232 168,178" fill="url(#ribbon-time)"/>
        <polygon class="accent" points="34,36 196,6 200,70 34,84"/>
        <text class="tag-label" x="44" y="74" transform="rotate(-9 44 74)">Study Brisk</text>
        <text class="claim" x="38" y="131" transform="rotate(-6 38 131)">Cut study time down</text>
        <text class="claim" x="44" y="177" transform="rotate(-6 44 177)">by up to 50%</text>
      </svg>
      <div class="megaphone" role="img" aria-label="Small megaphone illustration"></div>
    </div>

    <div class="banner banner--memory">
      <svg viewBox="0 0 372 275">
        <defs>
          <linearGradient id="ribbon-memory" x1="0" y1="1" x2="1" y2="0">
            <stop offset="0" class="stop-a"/><stop offset="1" class="stop-b"/>
          </linearGradient>
        </defs>
        <polygon points="0,84 352,33 352,153 0,202" fill="url(#ribbon-memory)"/>
        <polygon points="120,186 148,232 168,178" fill="url(#ribbon-memory)"/>
        <polygon class="accent" points="34,36 196,6 200,70 34,84"/>
        <text class="tag-label" x="44" y="74" transform="rotate(-9 44 74)">Study Brisk</text>
        <text class="claim" x="38" y="131" transform="rotate(-6 38 131)">Memorize anything</text>
        <text class="claim" x="44" y="177" transform="rotate(-6 44 177)">quickly</text>
        <polygon class="accent" points="228,160 330,140 330,188 228,201"/>
        <text class="free-label" x="255" y="188" transform="rotate(-6 255 188)">Free</text>
      </svg>
      <div class="megaphone" role="img" aria-label="Small megaphone illustration"></div>
    </div>

    <div class="banner banner--class">
      <svg viewBox="0 0 372 275">
        <defs>
          <linearGradient id="ribbon-class" x1="0" y1="1" x2="1" y2="0">
            <stop offset="0" class="stop-a"/><stop offset="1" class="stop-b"/>
          </linearGradient>
        </defs>
        <polygon points="0,84 352,33 352,153 0,202" fill="url(#ribbon-class)"/>
        <polygon points="120,186 148,232 168,178" fill="url(#ribbon-class)"/>
        <polygon class="accent" points="34,36 196,6 200,70 34,84"/>
        <text class="tag-label" x="44" y="74" transform="rotate(-9 44 74)">Study Brisk</text>
        <text class="claim" x="38" y="131" transform="rotate(-6 38 131)">Learn a subject without</text>
        <text class="claim" x="44" y="177" transform="rotate(-6 44 177)">having to go to class</text>
      </svg>
      <div class="megaphone" role="img" aria-label="Small megaphone illustration"></div>
    </div>
  </div>
</body>
</html>
```